Website design needed for Renewable utilities company based in New Zealand.

Website design needed for Lanternvale Holdings based in New Zealand.

Please see attached logo.

We sell solar panels, vertical axis wind turbines, atmospheric water generators and other related equipment for those who don't have access or don't want to depend on the government, city councils for their utilities (power and water).

We like metallic texture, dark grey and purple, red or blue colours. The design should go well with the attached logo.

Target Market(s)

The Eco conscious

Industry/Entity Type

Government

Logo Text

Lanternvale Summit

Requirements
Must have
• Must Have:
- Metallic finish is a must.
- Design should fit around the attached logo well.
Nice to have
• Sharpe design prefred rather than rounded edges

```html
<!DOCTYPE html>
<html lang="en">
<head>
<meta charset="utf-8">
<title>Lanternvale Summit</title>
<link rel="stylesheet" href="https://fonts.googleapis.com/css2?family=BenchNine:wght@300;400&family=Questrial&family=Arimo:wght@400&family=Tinos&display=swap">
<style>
:root{
  --page:#d6d6d6;
  --header-top:#f0f0f0;
  --header-bottom:#d0d0d0;
  --nav-text:#3a3a3a;
  --accent:#2a8fc0;
  --logo-blue:#1f7fb6;
  --ink:#333;
  --muted:#555;
  --line:#b9b9b9;
  --footer:#3d3d3d;
  --footer-text:#e6e6e6;
  --strip:#cbcbcb;
  --brush:repeating-linear-gradient(0deg,rgba(255,255,255,.16) 0 1px,rgba(0,0,0,.035) 1px 2px,transparent 2px 3px);
  --brush-v:repeating-linear-gradient(90deg,rgba(255,255,255,.1) 0 1px,transparent 1px 3px);
}
*{box-sizing:border-box;margin:0;padding:0}
html,body{width:1014px;height:1200px;overflow:hidden}
body{position:relative;background:var(--brush),var(--brush-v),var(--page);font-family:"Arimo",sans-serif;color:var(--ink)}
.site-header{position:absolute;left:0;top:0;width:1014px;height:108px;
  background:var(--brush),var(--brush-v),linear-gradient(var(--header-top),var(--header-bottom));z-index:2;
  box-shadow:0 1px 2px rgba(0,0,0,.2)}
.logo-notch{position:absolute;left:384px;top:60px;width:222px;height:86px;
  background:var(--brush),linear-gradient(#d2d2d2,#e4e4e4);border-radius:0 0 111px 111px / 0 0 86px 86px;
  box-shadow:0 3px 5px rgba(0,0,0,.25);z-index:3}
.logo{position:absolute;left:384px;top:24px;width:222px;text-align:center;z-index:4}
.logo-dot{display:block;width:54px;height:54px;margin:0 auto 16px;border-radius:50%;
  background:radial-gradient(circle at 40% 35%,#3b6fc4,#173a87)}
.logo-name{font-family:"Questrial",sans-serif;font-size:19px;color:var(--logo-blue)}
.main-nav{position:absolute;top:50px;left:0;width:1014px;z-index:4}
.main-nav a{position:absolute;font-family:"BenchNine",sans-serif;font-weight:300;font-size:18px;
  letter-spacing:2px;color:var(--nav-text);text-decoration:none}
.main-nav a.current{color:var(--accent)}
.hero{position:absolute;left:0;top:108px;width:1014px;height:465px;overflow:hidden;
  background:
    radial-gradient(ellipse 60% 30% at 30% 20%,rgba(220,230,240,.45),transparent 70%),
    linear-gradient(172deg,transparent 0 47%,rgba(20,30,55,.0) 47%,rgba(30,42,72,.9) 50%,#34466f 62%,#1d2740 100%),
    linear-gradient(180deg,#3c5c8e 0%,#6f8db4 30%,#a9bccf 48%,#8797ab 58%,#2a3550 100%);
  box-shadow:0 6px 10px rgba(0,0,0,.3)}
.hero-title{position:absolute;top:86px;width:100%;text-align:center;font-family:"Questrial",sans-serif;font-weight:400;
  font-size:31px;letter-spacing:3px;color:#f4f4f4}
.hero-caption{position:absolute;left:0;bottom:0;width:100%;height:128px;background:rgba(28,28,30,.72);
  padding:29px 126px 0;text-align:center;color:#f0f0f0;font-size:12px;line-height:24px;letter-spacing:.75px}
.products{position:absolute;left:70px;top:604px;width:605px;height:430px;
  background:var(--brush),linear-gradient(#ececec,#d3d3d3);
  border:1px solid #b9c6cf;border-radius:3px;box-shadow:0 1px 3px rgba(0,0,0,.15)}
.panel-title{height:34px;background:linear-gradient(#5fb0d6,#2c7fae);border-radius:3px 3px 0 0;
  padding-left:17px;font-family:"BenchNine",sans-serif;font-weight:300;font-size:21px;letter-spacing:2px;color:#fff;line-height:34px}
.categories{position:absolute;left:14px;top:50px;width:82px;text-align:center;font-family:"BenchNine",sans-serif;font-weight:300}
.category{margin-bottom:12px}
.category h3{font-weight:300;font-size:16px;letter-spacing:1.2px;color:var(--muted);padding-bottom:4px;border-bottom:1px dotted #999;margin-bottom:4px}
.category li{list-style:none;font-size:16px;line-height:20px;color:var(--muted);letter-spacing:1.2px}
.category li.active{color:var(--accent)}
.cat-divider{position:absolute;left:112px;top:50px;width:1px;height:365px;background:var(--line)}
.card{position:absolute;width:170px;text-align:center}
.card-image{display:block;width:170px;height:148px;border:2px solid #c9c9c9;background:linear-gradient(135deg,#e2e2e2,#d0d0d0);position:relative}
.card-image .panel-fill{position:absolute;left:22px;top:22px;width:126px;height:100px;background:linear-gradient(135deg,#3a4a88,#1d2356);transform:skewY(-18deg)}
.card-image .panel-fill.tall{left:44px;top:8px;width:80px;height:132px;transform:none}
.card p{margin-top:9px;font-family:"Tinos",serif;font-size:13px;letter-spacing:.9px;color:var(--muted)}
.scrollbar{position:absolute;left:592px;top:50px;width:5px;height:345px;background:#bbb;border-radius:3px}
.inquiry{position:absolute;left:726px;top:604px;width:247px}
.inquiry h2{font-family:"BenchNine",sans-serif;font-weight:300;font-size:20px;letter-spacing:1.8px;color:var(--ink);
  padding:0 0 8px 12px;border-bottom:1px solid #aaa;display:flex;align-items:center;gap:10px}
.field{position:absolute;font-family:"BenchNine",sans-serif;font-weight:300;font-size:18px;letter-spacing:1.8px;color:var(--muted)}
.input{position:absolute;left:63px;width:176px;background:#fff;border:1px solid #ccc;border-radius:3px}
.submit{position:absolute;left:63px;top:306px;width:176px;height:28px;border-radius:3px;background:linear-gradient(#6cb9dd,#2e82b0);
  color:#fff;text-align:center;line-height:28px;font-family:"BenchNine",sans-serif;font-weight:300;font-size:18px;letter-spacing:2px}
.social{position:absolute;left:68px;top:373px;display:flex;gap:11px}
.social span{width:28px;height:28px;display:block;background:linear-gradient(#8a97a5,#5e6b79)}
.contact-strip{position:absolute;left:0;top:1046px;width:1014px;height:104px;background:var(--brush),var(--brush-v),var(--strip)}
.contact{position:absolute;top:32px;display:flex;gap:10px;font-family:"BenchNine",sans-serif;font-weight:300;font-size:15px;letter-spacing:1.4px;line-height:19px;color:#444}
.contact b{font-weight:300;color:var(--accent)}
.site-footer{position:absolute;left:0;top:1150px;width:1014px;height:50px;background:var(--brush),var(--footer);color:var(--footer-text);font-size:12.5px;letter-spacing:1px}
.footer-nav{position:absolute;left:60px;top:21px}
.footer-nav span{margin:0 11px}
.copyright{position:absolute;right:54px;top:22px;font-size:10px;color:#aaa;letter-spacing:.8px}
</style>
</head>
<body>
<header class="site-header">
  <nav class="main-nav">
    <a class="current" style="left:76px">Home</a>
    <a style="left:176px">About us</a>
    <a style="left:299px">Our Products</a>
    <a style="left:607px">Promos</a>
    <a style="left:721px">Testimonials</a>
    <a style="left:868px">Contact us</a>
  </nav>
</header>
<div class="logo-notch"></div>
<div class="logo"><span class="logo-dot"></span><span class="logo-name">Lanternvale Summit</span></div>

<section class="hero" role="img" aria-label="Workers installing solar panels on a rooftop under a blue sky">
  <h1 class="hero-title">Lanternvale Summit Solar Panels</h1>
  <p class="hero-caption">Lorem ipsum dolor sit amet, consectetur adipiscing elit. Curabitur blandit diam id laoreet tristique. Praesent tempor in purus in imperdiet. Quisque lobortis sapien vitae nibh bibendum ullamcorper. Lorem ipsum dolor sit amet, consectetur adipiscing elit. Duis dapibus magna lectus, ac sagittis eros dictum a.</p>
</section>

<section class="products">
  <div class="panel-title">Our Products</div>
  <div class="categories">
    <div class="category"><h3>Categy 1</h3><ul><li class="active">-Item</li><li>-Item</li><li>-Item</li></ul></div>
    <div class="category"><h3>Categy 2</h3><ul><li>-Item</li><li>-Item</li><li>-Item</li></ul></div>
    <div class="category"><h3>Categy 3</h3><ul><li>-Item</li><li>-Item</li><li>-Item</li></ul></div>
  </div>
  <div class="cat-divider"></div>
  <div class="card" style="left:145px;top:43px"><span class="card-image"><span class="panel-fill" role="img" aria-label="Solar panel product photo"></span></span><p>Product name (24x24)</p></div>
  <div class="card" style="left:349px;top:43px"><span class="card-image"><span class="panel-fill" role="img" aria-label="Solar panel product photo"></span></span><p>Product name (36x42)</p></div>
  <div class="card" style="left:145px;top:238px"><span class="card-image"><span class="panel-fill tall" role="img" aria-label="Upright solar panel product photo"></span></span><p>Product name (24x24)</p></div>
  <div class="card" style="left:354px;top:238px"><span class="card-image"><span class="panel-fill tall" role="img" aria-label="Upright solar panel product photo"></span></span><p>Product name (24x24)</p></div>
  <div class="scrollbar"></div>
</section>

<aside class="inquiry">
  <h2>Get an Inquiry now
    <svg width="22" height="18" viewBox="0 0 22 18"><path d="M2 10l6 6L20 2" fill="none" stroke="#3b97c9" stroke-width="4"/></svg>
  </h2>
  <span class="field" style="left:22px;top:50px">Name</span><div class="input" style="top:48px;height:28px"></div>
  <span class="field" style="left:22px;top:93px">Email</span><div class="input" style="top:90px;height:28px"></div>
  <span class="field" style="left:5px;top:138px">Message</span><div class="input" style="top:141px;height:149px"></div>
  <div class="submit">Submit</div>
  <div class="social" aria-label="Social links"><span></span><span></span><span></span><span></span></div>
</aside>

<section class="contact-strip">
  <div class="contact" style="left:77px">
    <svg width="20" height="18" viewBox="0 0 20 18"><path d="M10 1L1 9h3v8h12V9h3z" fill="#8a8a8a"/></svg>
    <div><b>Address:</b> 1111 Street ,<br>City name, Country</div>
  </div>
  <div class="contact" style="left:270px">
    <svg width="22" height="26" viewBox="0 0 22 26"><path d="M5 1l4 6-3 3c1 4 4 8 8 10l3-3 5 4-3 4C9 25 1 15 1 5z" fill="#8a8a8a"/></svg>
    <div><b>Phone:</b> 1-800-111-1111<br>&nbsp;&nbsp;&nbsp;&nbsp;&nbsp;&nbsp;&nbsp;&nbsp;&nbsp;: 1-800-222-1111</div>
  </div>
  <div class="contact" style="left:517px">
    <svg width="28" height="24" viewBox="0 0 28 24"><rect x="7" y="1" width="14" height="7" fill="#8a8a8a"/><rect x="1" y="7" width="26" height="11" rx="2" fill="#8a8a8a"/><rect x="7" y="14" width="14" height="9" fill="#cfcfcf" stroke="#8a8a8a" stroke-width="2"/></svg>
    <div><b>Fax:</b> 1-800-111-1112<br>&nbsp;&nbsp;&nbsp;&nbsp;&nbsp;: 1-800-222-1112</div>
  </div>
  <div class="contact" style="left:784px">
    <svg width="24" height="16" viewBox="0 0 24 16"><rect width="24" height="16" fill="#8a8a8a"/><path d="M0 0l12 9 12-9" fill="none" stroke="#cfcfcf" stroke-width="1.5"/></svg>
    <div><b>Email:</b> your@email.com</div>
  </div>
</section>

<footer class="site-footer">
  <div class="footer-nav">Home<span>|</span>About us<span>|</span>Our Products<span>|</span>Promos<span>|</span>Testimonials</div>
  <div class="copyright">Copyright © 2013 Lanternvale Summit</div>
</footer>
</body>
</html>
```